Consulting company needs Business Cards - rough concept provided

I'm looking for someone to take our business card idea and make is slick and polished - to communicate our high-end, sophisticated, serious consulting business. We have a rough layout we did in-house. We are open to ideas on repo-ing elements, adjusting sizes, typefaces etc... within the general concept we've already come up with. We want it to be super-clean and sophisticated. We want to keep the white backgrounds, and blue brand colors. Our goal is to print with painted blue edges on thick cardstock. Thank you!!

```html
<!DOCTYPE html>
<html lang="en">
<head>
<meta charset="utf-8">
<title>Kestrel – Business Card</title>
<link rel="stylesheet" href="https://fonts.googleapis.com/css2?family=Poppins:wght@200;400;600;700&display=swap">
<style>
  :root {
    --brand-blue: #0a8ed3;
    --paper-white: #f7f7f7;
    --backdrop: #dcd9d6;
    --card-shadow: rgba(0, 0, 0, 0.18);
    --ink-grey: #555555;
  }
  * { margin: 0; padding: 0; box-sizing: border-box; }
  html, body {
    width: 936px;
    height: 1200px;
    overflow: hidden;
  }
  body {
    background: var(--backdrop);
    font-family: "Poppins", sans-serif;
    position: relative;
  }
  .card {
    position: absolute;
    left: 48px;
    width: 840px;
    height: 480px;
    background: var(--paper-white);
    box-shadow: 0 4px 14px var(--card-shadow);
    overflow: hidden;
  }
  .card--front { top: 100px; }
  .card--back { top: 640px; }

  /* Front */
  .brand-strip {
    position: absolute;
    left: 0; top: 0;
    width: 297px; height: 100%;
    background: var(--paper-white);
    display: flex;
    align-items: center;
    justify-content: center;
    gap: 12px;
  }
  .brand-mark {
    width: 18px;
    height: 18px;
    background: var(--brand-blue);
    flex: none;
  }
  .brand-name {
    font-weight: 600;
    font-size: 38px;
    line-height: 1;
    color: var(--brand-blue);
    white-space: nowrap;
  }
  .contact-panel {
    position: absolute;
    left: 297px; top: 0;
    width: 543px; height: 100%;
    background: var(--brand-blue);
    color: #ffffff;
  }
  .person-name {
    position: absolute;
    left: 83px; top: 54px;
    font-weight: 700;
    font-size: 29px;
    line-height: 1;
  }
  .person-title {
    position: absolute;
    left: 83px; top: 98px;
    font-weight: 400;
    font-size: 17px;
    line-height: 1;
  }
  .address {
    position: absolute;
    left: 90px; top: 278px;
    font-size: 18px;
    line-height: 25px;
    font-weight: 400;
  }
  .contact-list {
    position: absolute;
    left: 90px; top: 354px;
    list-style: none;
    font-size: 19px;
    line-height: 25px;
  }
  .contact-list li {
    display: flex;
    align-items: center;
    gap: 16px;
  }
  .contact-icon { width: 14px; height: 14px; fill: #ffffff; flex: none; }

  /* Back */
  .accent-bar {
    position: absolute;
    left: 0; top: 70px;
    width: 15px; height: 348px;
    background: var(--brand-blue);
  }
  .pledge-line {
    position: absolute;
    left: 54px;
    line-height: 1;
    white-space: nowrap;
    color: var(--ink-grey);
    font-weight: 200;
    font-size: 39px;
  }
  .pledge-key {
    color: var(--brand-blue);
    font-weight: 700;
    font-size: 44px;
  }
  .line-1 { top: 67px; }
  .line-2 { top: 118px; }
  .line-3 { top: 184px; }
  .line-4 { top: 242px; }
  .line-5 { top: 308px; }
  .line-6 { top: 378px; }
</style>
</head>
<body>

<section class="card card--front" aria-label="Business card front">
  <div class="brand-strip">
    <span class="brand-mark" aria-hidden="true"></span>
    <span class="brand-name">Kestrel</span>
  </div>
  <div class="contact-panel">
    <p class="person-name">Dana Whitlow</p>
    <p class="person-title">Brand Consultant</p>
    <p class="address">4820 Larkin Ave, Ste210<br>Fairmont, CA 90412</p>
    <ul class="contact-list">
      <li>
        <svg class="contact-icon" viewBox="0 0 24 24" aria-hidden="true"><path d="M6.6 10.8a15.1 15.1 0 0 0 6.6 6.6l2.2-2.2a1 1 0 0 1 1-.25 11.4 11.4 0 0 0 3.6.57 1 1 0 0 1 1 1V20a1 1 0 0 1-1 1A17 17 0 0 1 3 4a1 1 0 0 1 1-1h3.5a1 1 0 0 1 1 1c0 1.25.2 2.45.57 3.57a1 1 0 0 1-.25 1z"/></svg>
        <span>(555) 014 2280</span>
      </li>
      <li>
        <svg class="contact-icon" viewBox="0 0 24 24" aria-hidden="true"><path d="M2 5h20v14H2z M3.5 6.5 12 13l8.5-6.5" fill="#ffffff" stroke="var(--brand-blue)" stroke-width="1.6"/></svg>
        <span>dana@kestrelco.com</span>
      </li>
      <li>
        <svg class="contact-icon" viewBox="0 0 24 24" aria-hidden="true"><circle cx="12" cy="12" r="10"/><path d="M2 12h20M12 2c3 3 3 17 0 20M12 2c-3 3-3 17 0 20" fill="none" stroke="var(--brand-blue)" stroke-width="1.4"/></svg>
        <span>dana@kestrelco.com</span>
      </li>
    </ul>
  </div>
</section>

<section class="card card--back" aria-label="Business card back">
  <div class="accent-bar"></div>
  <p class="pledge-line line-1"><span class="pledge-key">WE HELP</span></p>
  <p class="pledge-line line-2">[TARGET DEMOGRAPHIC]</p>
  <p class="pledge-line line-3"><span class="pledge-key">ACHIEVE</span></p>
  <p class="pledge-line line-4">[DESIRED EMOTIONAL OUTCOME]</p>
  <p class="pledge-line line-5"><span class="pledge-key">BY</span> [OUR UNIQUE APPROACH]</p>
  <p class="pledge-line line-6"><span class="pledge-key">BECAUSE</span> [OUR BRAND BELIEFS]</p>
</section>

</body>
</html>
```